Letterhead for clinic notes, test reports, and business cards

I need business card and letterheads for a medical clinic with the following:
1- Business cards. The back should allow for space for date and time of next appointments (few lines would do)
2- Letterhead for clinic notes
3- Letterhead for test reports.

Feel free to use whats included for examples. I value creativity so be creative.

Target Market(s)

Patients, referring physicians.

Industry/Entity Type

Health Care

Requirements
Must have
• Must use current logo.
• Must look good on white background
• Letterhead and reports must look good faxed.
• Please use themes of the current logo. Another possible color to use is grey as well (www.brambleveincare.org - use the font color in the text of that website)

```html
<!DOCTYPE html>
<html lang="en">
<head>
<meta charset="UTF-8">
<title>Bramblevein Care Institute – Business Card</title>
<link href="https://fonts.googleapis.com/css2?family=Open+Sans:wght@400;600;700&display=swap" rel="stylesheet">
<style>
  :root {
    --bg: #2a2a2c;
    --card: #ffffff;
    --navy: #1f3f8f;
    --blue: #2f74c8;
    --red: #c62f36;
    --text: #5a5d63;
    --link: #2f6fc4;
    --rule: #8d9096;
  }
  * { box-sizing: border-box; margin: 0; padding: 0; }
  html, body { width: 1200px; height: 950px; overflow: hidden; }
  body {
    background: var(--bg);
    font-family: "Open Sans", Arial, sans-serif;
    display: flex; flex-direction: column; align-items: center; justify-content: center;
    gap: 40px;
  }
  .card {
    position: relative; width: 760px; height: 434px;
    background: var(--card); overflow: hidden;
  }
  .card-front .band { position: absolute; inset: 0; width: 100%; height: 100%; }
  .holder { position: absolute; left: 36px; top: 290px; color: #fff; }
  .holder-name { font-size: 24px; font-weight: 600; line-height: 1.2; }
  .holder-title { font-size: 16px; opacity: .9; }
  .brand {
    position: absolute; left: 390px; top: 64px;
    display: flex; align-items: center; gap: 14px;
  }
  .brand-dot { width: 30px; height: 30px; border-radius: 50%; background: var(--red); flex: none; }
  .brand-name {
    font-size: 26px; font-weight: 600; color: var(--navy);
    line-height: 1.15; text-transform: uppercase; letter-spacing: 1px;
  }
  .address {
    position: absolute; right: 40px; top: 180px; text-align: right;
    font-style: normal; font-size: 17px; color: var(--text); line-height: 1.5;
  }
  .address .web { color: var(--link); }
  .contacts {
    position: absolute; left: 330px; bottom: 36px; list-style: none;
    font-size: 17px; color: var(--text); line-height: 1.65;
  }
  .contacts li { display: flex; align-items: center; gap: 10px; }
  .contacts svg { width: 15px; height: 15px; fill: var(--navy); flex: none; }

  .card-back { padding: 30px 44px; color: var(--text); }
  .appt-title {
    text-align: center; font-size: 28px; font-weight: 700; color: var(--navy);
    margin-bottom: 22px;
  }
  .field {
    display: flex; align-items: flex-end; gap: 10px;
    height: 56px; padding-bottom: 2px; border-bottom: 1.5px solid var(--rule);
    font-size: 18px; font-style: italic; color: var(--navy);
  }
  .field-row { display: flex; gap: 40px; }
  .field-row .field { flex: 1; }
  .ampm { margin-left: auto; font-size: 14px; color: var(--link); }
  .note {
    margin-top: 30px; text-align: center; font-size: 15px; font-style: italic; color: #333;
  }
</style>
</head>
<body>
  <section class="card card-front">
    <svg class="band" viewBox="0 0 760 434" preserveAspectRatio="none" aria-hidden="true">
      <defs>
        <linearGradient id="bandBlue" x1="0" y1="0" x2="1" y2="1">
          <stop offset="0" stop-color="#2f7dd0"/>
          <stop offset="1" stop-color="#1c3a8c"/>
        </linearGradient>
      </defs>
      <path d="M0 0 H372 C318 90 286 200 284 340 L182 434 H0 Z" fill="var(--red)"/>
      <path d="M0 0 H352 C300 90 270 200 268 326 L168 434 H0 Z" fill="url(#bandBlue)"/>
    </svg>
    <div class="holder">
      <p class="holder-name">Mara Ellison</p>
      <p class="holder-title">President</p>
    </div>
    <div class="brand">
      <span class="brand-dot"></span>
      <p class="brand-name">Bramblevein Care<br>Institute</p>
    </div>
    <address class="address">
      1820 Larkfield Avenue<br>
      Suite 201, Ashbury ON K4R2M7<br>
      <span class="web">www.brambleveincare.org</span>
    </address>
    <ul class="contacts">
      <li><svg viewBox="0 0 16 16"><path d="M3 1l3 3-2 2c1 2 3 4 5 5l2-2 3 3-2 3C6 15 1 10 1 3z"/></svg>555.204.1187</li>
      <li><svg viewBox="0 0 16 16"><rect x="1" y="5" width="14" height="9" rx="1"/><rect x="4" y="1" width="8" height="5"/></svg>555.318.9052</li>
      <li><svg viewBox="0 0 16 16"><path d="M1 3h14v10H1z M1 3l7 6 7-6" stroke="#fff" stroke-width="1"/></svg>contact@brambleveincare.org</li>
    </ul>
  </section>

  <section class="card card-back">
    <h2 class="appt-title">Next Appointment</h2>
    <div class="field">For :</div>
    <div class="field-row">
      <div class="field">Date :</div>
      <div class="field">Time : <span class="ampm">AM/PM</span></div>
    </div>
    <div class="field">Dr :</div>
    <p class="note">To cancel your appointment please call the office 24 hours in advance.</p>
  </section>
</body>
</html>
```